Therapy Services & Training

I provide counseling/therapy to individuals and families. I also travel the country and provide training at conferences.
I would like to see a card which takes my company name and design a logo using the letters "HWAE".
Target Market(s)
Therapists, non-profit organizations, clients looking for therapy
Industry/Entity Type
Training
Contact Information for Business Card
Harborview Wellness Advising & Education LLC
Delia Marsh, M.S.W., LCSW
Clinical Therapist & Trainer
Providing clinical therapy services to individuals, families, couples & children. We also provide life coaching and crisis training.
counselordelia@mailbrook.net
www.harborviewwellnessadvising.com
(555) 214-3092
Fernwood, IL 60000
(BACK SIDE OF CARD)
We are certified by the Ongoing Professional Lawyer Studies (OPLS) Council of the Prairie High Tribunal to provide Continuing Legal Education (CLE) credits to Illinois attorneys. Call about what courses we offer! (555) 214-3092

```html
<!DOCTYPE html>
<html lang="en">
<head>
<meta charset="utf-8">
<title>Harborview Wellness Advising &amp; Education — Business Card</title>
<link rel="stylesheet" href="https://fonts.googleapis.com/css2?family=Pathway+Gothic+One&family=Saira+Condensed:wght@600&display=swap">
<style>
  :root {
    --page: #ece9e4;
    --green-dark: #2e7d3a;
    --green-mid: #7fc46f;
    --green-light: #a9d79a;
    --green-pale: #c4e4b8;
    --white: #ffffff;
    --shadow: rgba(0, 0, 0, 0.28);
  }
  * { margin: 0; padding: 0; box-sizing: border-box; }
  html, body { width: 1200px; height: 1000px; overflow: hidden; }
  body {
    background: var(--page);
    position: relative;
    font-family: "Saira Condensed", "Pathway Gothic One", sans-serif;
    font-weight: 600;
  }
  .card {
    position: absolute;
    left: 275px;
    width: 650px;
    height: 385px;
    box-shadow: 0 6px 18px var(--shadow);
    overflow: hidden;
  }

  /* Back side */
  .card--back {
    top: 70px;
    background: radial-gradient(ellipse at 55% 55%, var(--green-mid) 0%, var(--green-light) 80%, var(--green-pale) 100%);
  }
  .back__panel {
    position: absolute;
    left: 157px;
    top: 0;
    width: 355px;
    height: 225px;
    background: var(--white);
    border-radius: 0 0 10px 10px;
    box-shadow: 6px 6px 10px var(--shadow);
    display: flex;
    flex-direction: column;
    align-items: center;
    justify-content: center;
  }
  .brand {
    display: flex;
    align-items: center;
    gap: 12px;
    color: var(--green-dark);
    font-family: "Pathway Gothic One", sans-serif;
    font-weight: 400;
    font-size: 96px;
    line-height: 1;
  }
  .brand__square {
    width: 22px;
    height: 22px;
    background: var(--green-mid);
  }
  .back__web {
    margin-top: 26px;
    font-size: 13px;
    color: var(--green-dark);
  }
  .back__statement {
    position: absolute;
    left: 40px;
    top: 250px;
    width: 580px;
    font-family: "Pathway Gothic One", sans-serif;
    font-weight: 400;
    font-size: 17px;
    line-height: 1.25;
    color: var(--white);
    text-shadow: 1px 1px 2px rgba(0, 0, 0, 0.3);
  }
  .back__phone {
    position: absolute;
    left: 0;
    right: 0;
    top: 310px;
    text-align: center;
    font-family: "Pathway Gothic One", sans-serif;
    font-weight: 400;
    font-size: 40px;
    color: var(--white);
    text-shadow: 1px 1px 2px rgba(0, 0, 0, 0.3);
  }

  /* Front side */
  .card--front {
    top: 525px;
    background: var(--white);
  }
  .front__ornament {
    position: absolute;
    left: 0;
    top: 190px;
    width: 340px;
    height: 110px;
    background: linear-gradient(100deg, var(--green-pale) 0%, var(--green-light) 45%, var(--green-mid) 100%);
    opacity: 0.85;
  }
  .front__logo {
    position: absolute;
    left: 70px;
    top: 30px;
    width: 240px;
  }
  .front__logo .brand { font-size: 84px; }
  .front__company {
    margin-top: 8px;
    font-size: 13px;
    color: var(--green-dark);
    white-space: nowrap;
  }
  .front__details {
    position: absolute;
    right: 30px;
    top: 60px;
    text-align: right;
    color: var(--green-dark);
  }
  .front__name { font-size: 24px; line-height: 1.2; }
  .front__creds { font-size: 16px; }
  .front__title { font-size: 15px; color: var(--green-mid); margin-bottom: 14px; }
  .front__contact { font-size: 17px; line-height: 1.6; }
  .front__web { font-size: 18px; margin-top: 10px; }
  .front__tagline {
    position: absolute;
    right: 30px;
    bottom: 26px;
    text-align: right;
    font-size: 13px;
    line-height: 1.6;
    color: var(--green-dark);
  }
</style>
</head>
<body>

<section class="card card--back" aria-label="Back of business card">
  <div class="back__panel">
    <div class="brand"><span class="brand__square"></span>HWAE</div>
    <p class="back__web">www.harborviewwellnessadvising.com</p>
  </div>
  <p class="back__statement">We are certified by the Ongoing Professional Lawyer Studies (OPLS) Council of the Prairie High Tribunal to provide Continuing Legal Education (CLE) credits to Illinois attorneys. Call about what courses we offer!</p>
  <p class="back__phone">(555) 214-3092</p>
</section>

<section class="card card--front" aria-label="Front of business card">
  <div class="front__ornament" role="img" aria-label="Decorative green wave ornament"></div>

  <div class="front__logo">
    <div class="brand"><span class="brand__square"></span>HWAE</div>
    <p class="front__company">Harborview Wellness Advising &amp; Education LLC</p>
  </div>

  <div class="front__details">
    <p class="front__name">Delia Marsh, <span class="front__creds">M.S.W., LCSW</span></p>
    <p class="front__title">Clinical Therapist &amp; Trainer</p>
    <p class="front__contact">(555) 214-3092 Fernwood, IL 60000<br>counselordelia@mailbrook.net</p>
    <p class="front__web">www.harborviewwellnessadvising.com</p>
  </div>

  <p class="front__tagline">Providing clinical therapy services to individuals, families, couples &amp; children.<br>We also provide life coaching and crisis training.</p>
</section>

</body>
</html>
```